terras letterhead

We would like to create a new letterhead that our company will use for proposals, invoices, statements and letters. Our company name is Terra-Vantage. We are a landscape design/build and landscape maintenance company. We have a web site Terra-Vantage.example where our logo (the leaf with the lettering within it only) is displayed.

Industry/Entity Type

Graphic Design

Requirements
Must have
• Address and info on our current letterhead (uploaded)
Nice to have
• We would like the design to look presentable in grey scale as well as color.
Should not have
• Do not want to infringe much on the normal useable area within the normal print areas.

```html
<!DOCTYPE html>
<html lang="en">
<head>
<meta charset="utf-8">
<title>Terra-Vantage Letterhead</title>
<link href="https://fonts.googleapis.com/css2?family=Arimo:wght@400&family=Questrial&display=swap" rel="stylesheet">
<style>
  :root {
    --backdrop: #17693a;
    --paper: #ffffff;
    --ink: #111111;
    --brand-green: #1f3b1d;
    --brand-green-soft: #2e4f2a;
  }
  * { margin: 0; padding: 0; box-sizing: border-box; }
  html, body {
    width: 1200px;
    height: 848px;
    overflow: hidden;
    background: var(--backdrop);
  }
  .sheet {
    position: absolute;
    left: 319px;
    top: 27px;
    width: 561px;
    height: 793px;
    background: var(--paper);
  }
  .brand {
    position: absolute;
    left: 38px;
    top: 83px;
    display: flex;
    align-items: center;
    gap: 6px;
  }
  .brand-dot {
    width: 10px;
    height: 10px;
    border-radius: 50%;
    background: var(--brand-green);
  }
  .brand-name {
    font-family: "Questrial", sans-serif;
    font-weight: 400;
    font-size: 14px;
    color: var(--brand-green);
  }
  .letter-body {
    position: absolute;
    left: 58px;
    top: 185px;
    width: 447px;
    font-family: "Arimo", Arial, sans-serif;
    font-size: 8.4px;
    line-height: 12.9px;
    color: var(--ink);
    text-align: justify;
  }
  .letter-body p + p { margin-top: 12.9px; }
  .signature {
    position: absolute;
    left: 53px;
    top: 463px;
    width: 58px;
    height: 36px;
    background: linear-gradient(135deg, #e6e6e6, #cfcfcf);
  }
  .contact {
    position: absolute;
    left: 58px;
    top: 680px;
    font-family: "Questrial", sans-serif;
    font-size: 7.4px;
    line-height: 9px;
    color: var(--ink);
  }
  .contact-group + .contact-group { margin-top: 4px; }
  .contact b { font-weight: 700; }
  .tree {
    position: absolute;
    left: 387px;
    top: 635px;
    width: 136px;
    height: 121px;
    border-radius: 48% 48% 10% 10%;
    background: radial-gradient(ellipse at 50% 40%, var(--brand-green-soft), var(--brand-green));
  }
</style>
</head>
<body>
  <main class="sheet">
    <header class="brand">
      <span class="brand-dot"></span>
      <span class="brand-name">Terra-Vantage</span>
    </header>

    <section class="letter-body">
      <p>Lorem ipsum dolor sit amet, consectetur adipiscing elit. Suspendisse blandit, nulla ut porta scelerisque, urna massa ultrices ligula, at rutrum nunc ipsum ac risus. Sed consectetur nulla non velit sollicitudin a eleifend tortor pellentesque. Cras laoreet iaculis pretium. Vestibulum vitae sapien at metus fermentum tempus quis sed mauris. Donec blandit metus in nibh laoreet ultrices. Nullam molestie, turpis ac adipiscing tincidunt, urna justo eleifend ligula, et consectetur massa lorem ac risus. Aenean quis justo vitae massa accumsan ultricies posuere eget diam. Aenean ipsum sapien, pellentesque id semper vitae, mattis eget enim. Vestibulum congue tincidunt enim ut tristique. Praesent interdum malesuada adipiscing. Donec quis felis massa.</p>
      <p>Praesent nisi libero, pretium eu interdum eu, rhoncus ut lorem. Praesent faucibus lorem sit amet ligula consequat adipiscing. Morbi adipiscing dapibus erat, eu condimentum nibh vestibulum vel. In elementum nulla id arcu bibendum malesuada. Donec non nulla sit amet tortor volutpat placerat id vel felis. Maecenas accumsan, augue ac molestie iaculis, justo risus vestibulum dolor, eu ullamcorper nulla orci ac est. Donec tristique sem a nisl euismod convallis id ac lacus. Sed pretium bibendum velit eget mollis. Praesent porta suscipit lacus, ac porta odio faucibus eu. Donec accumsan laoreet nisi et hendrerit. In fringilla enim ac urna sagittis convallis.</p>
      <p>Nullam est mi, euismod ac pretium ac, consequat eu urna. Aliquam egestas, elit non gravida pellentesque, purus orci facilisis est, vitae ultrices turpis nisl non justo. Fusce varius libero nec nibh elementum consequat ut sed elit. Integer lorem erat, varius ac malesuada vitae, convallis sit amet libero. Cras sagittis, urna eu scelerisque auctor, elit tellus vestibulum mi, non elementum metus eros ut dolor. Etiam porta est dolor. Vivamus suscipit lobortis commodo. Integer convallis, nunc tincidunt rhoncus lobortis, sapien purus ultrices orci, quis dignissim urna felis dictum elit.</p>
    </section>

    <div class="signature" role="img" aria-label="Handwritten signature"></div>

    <footer class="contact">
      <div class="contact-group">18 Orchard Lane<br>Fernbrook, OR 97000</div>
      <div class="contact-group"><b>t.</b> (555) 010-2468<br><b>f.</b> (555) 010-3579</div>
      <div class="contact-group"><b>e.</b> service@terra-vantage.example<br><b>w.</b> www.terra-vantage.example</div>
    </footer>

    <div class="tree" role="img" aria-label="Dark green silhouette illustration of a broad oak tree on a patch of grass"></div>
  </main>
</body>
</html>
```